Einladungskarte
Zielgruppe
Hochzeitsgäste zwischen 30 und 40
Aufgabenstellung
Die Einladung hat folgende Eckdaten:
- Format Din A5 (Doppelseitiger DinA 4 gefalzt) Einladungsbogen (wird leichter Karton)
- Zusätzlicher Einlagebogen für Einladungstext
- Stil klassisch/elegant eher schlicht aber jung
- Grundthema Gerberablume (weiß, beige, rot oder orange)
- Hintergrund (hell)
- Zusätzlich zur Einladung wird Bildrecht der Blume für ein Banner auf der Hochzeitswebseite benötigt
- Editierbare Graphikdatei wird benötigt (da der Text der Einladung noch nicht final ist)

```html
<!DOCTYPE html>
<html lang="de">
<head>
<meta charset="utf-8">
<title>Einladung zur Hochzeit</title>
<link rel="stylesheet" href="https://fonts.googleapis.com/css2?family=Barlow:wght@500;600&display=swap">
<style>
  :root {
    --page-bg: #efefef;
    --card-bg: #ffffff;
    --wine: #8a1538;
    --wine-dark: #4a0a1e;
    --petal: #b0294f;
    --pollen: #b59a3a;
    --text-grey: #9b9b9b;
  }
  * { margin: 0; padding: 0; box-sizing: border-box; }
  html, body {
    width: 1200px;
    height: 845px;
    overflow: hidden;
    background: var(--page-bg);
  }
  .canvas {
    position: relative;
    width: 1200px;
    height: 845px;
  }
  .card-front {
    position: absolute;
    left: 331px;
    top: 42px;
    width: 538px;
    height: 760px;
    background: var(--card-bg);
  }
  .flower-band {
    position: absolute;
    left: 0;
    top: 108px;
    width: 538px;
    height: 237px;
    display: block;
  }
  .invitation-title {
    position: absolute;
    left: 53px;
    top: 360px;
    font-family: "Barlow", sans-serif;
    font-weight: 600;
    font-size: 52px;
    line-height: 1;
    color: var(--wine);
    letter-spacing: 0.2px;
  }
  .invitation-subline {
    position: absolute;
    left: 53px;
    top: 436px;
    font-family: "Barlow", sans-serif;
    font-weight: 600;
    font-size: 25px;
    line-height: 34px;
    color: var(--text-grey);
  }
</style>
</head>
<body>
  <main class="canvas">
    <section class="card-front">
      <svg class="flower-band" viewBox="0 0 538 237" role="img" aria-label="Nahaufnahme einer dunkelroten Gerberablüte mit gelben Staubgefäßen">
        <defs>
          <radialGradient id="bloom" cx="0.48" cy="0.3" r="0.75">
            <stop offset="0" stop-color="var(--pollen)"/>
            <stop offset="0.22" stop-color="var(--wine-dark)"/>
            <stop offset="0.6" stop-color="var(--wine)"/>
            <stop offset="1" stop-color="var(--petal)"/>
          </radialGradient>
        </defs>
        <rect width="538" height="237" fill="url(#bloom)"/>
      </svg>
      <h1 class="invitation-title">Einladung</h1>
      <p class="invitation-subline">zur Hochzeit von<br>Mara &amp; Jonas</p>
    </section>
  </main>
</body>
</html>
```